business card design

i would like business cards designed. My business provides trade qualified personnel to the mining industry to work on heavy mobile equipment.
please put a excavator(digger) in the background in one design and have one design without so i can compare the difference.
also add info:
my logo(attached) and "mobile equipment repair and maintenance"
name: Derek Holloway
address: 57 Tarrowby RD Carmel Perth WA.
mobile: 0438120957
email: derek@ironvalemx.com

```html
<!DOCTYPE html>
<html lang="en">
<head>
<meta charset="utf-8">
<title>Ironvale Maintenance Services – Business Card</title>
<link rel="stylesheet" href="https://fonts.googleapis.com/css2?family=Arimo&family=Lexend:wght@500&family=Montserrat:wght@500;600;800&display=swap">
<style>
  :root {
    --backdrop: #e5e5e5;
    --card-white: #ffffff;
    --navy: #28334c;
    --steel-blue: #4e77bc;
    --deep-blue: #3f5ca8;
    --text-light: #ffffff;
  }
  * { box-sizing: border-box; margin: 0; padding: 0; }
  html, body {
    width: 1200px;
    height: 1200px;
    overflow: hidden;
    background: var(--backdrop);
  }
  .card {
    position: absolute;
    left: 243px;
    width: 712px;
    height: 410px;
    border-radius: 31px;
    overflow: hidden;
  }
  .card-front { top: 157px; background: var(--card-white); }
  .card-back  { top: 653px; background: var(--navy); }

  .front-shapes { position: absolute; inset: 0; }

  .brand-name {
    position: absolute;
    top: 128px;
    left: 0;
    width: 100%;
    text-align: center;
    font-family: "Montserrat", sans-serif;
    font-weight: 800;
    font-size: 64px;
    line-height: 64px;
    letter-spacing: 6px;
    color: var(--navy);
  }
  .brand-sub {
    position: absolute;
    top: 193px;
    left: 0;
    width: 100%;
    text-align: center;
    font-family: "Montserrat", sans-serif;
    font-weight: 600;
    font-size: 15px;
    letter-spacing: 2.2px;
    color: var(--steel-blue);
  }
  .tagline {
    position: absolute;
    top: 256px;
    left: 0;
    width: 100%;
    text-align: center;
    font-family: "Lexend", sans-serif;
    font-weight: 500;
    font-size: 19.5px;
    letter-spacing: -0.3px;
    color: var(--text-light);
  }

  .holder-name {
    position: absolute;
    left: 62px;
    top: 78px;
    font-family: "Montserrat", sans-serif;
    font-weight: 600;
    font-size: 36px;
    letter-spacing: -0.5px;
    color: var(--text-light);
  }
  .name-rule {
    position: absolute;
    left: 65px;
    top: 134px;
    width: 545px;
    height: 1px;
    background: var(--steel-blue);
  }
  .contact-list {
    position: absolute;
    left: 64px;
    top: 266px;
    list-style: none;
    font-family: "Arimo", sans-serif;
    font-size: 20px;
    color: var(--text-light);
  }
  .contact-item {
    display: flex;
    align-items: center;
    height: 28px;
  }
  .contact-item + .contact-item { margin-top: 8px; }
  .contact-item:last-child { margin-top: 5px; }
  .contact-icon {
    width: 18px;
    height: 20px;
    margin-right: 12px;
    flex: none;
  }
</style>
</head>
<body>

<section class="card card-front" aria-label="Card front">
  <svg class="front-shapes" width="712" height="410" viewBox="0 0 712 410" aria-hidden="true">
    <polygon points="0,172 163,332 0,332" fill="var(--steel-blue)"/>
    <polygon points="712,180 554,332 712,332" fill="var(--steel-blue)"/>
    <polygon points="130,300 196,300 163,332" fill="var(--deep-blue)"/>
    <polygon points="521,300 588,300 554,332" fill="var(--deep-blue)"/>
    <polygon points="73,243 646,243 588,300 130,300" fill="var(--navy)"/>
  </svg>
  <div class="brand-name">IRONVALE</div>
  <div class="brand-sub">MAINTENANCE SERVICES PTY LTD</div>
  <div class="tagline">Mobile Equipment Repair and Maintenance</div>
</section>

<section class="card card-back" aria-label="Card back">
  <h1 class="holder-name">DEREK HOLLOWAY</h1>
  <div class="name-rule"></div>
  <ul class="contact-list">
    <li class="contact-item">
      <svg class="contact-icon" viewBox="0 0 18 20" aria-hidden="true">
        <path d="M9 1a7 7 0 0 0-7 7c0 5 7 11 7 11s7-6 7-11a7 7 0 0 0-7-7zm0 10a3 3 0 1 1 0-6 3 3 0 0 1 0 6z" fill="var(--text-light)"/>
      </svg>
      <span>57 Tarrowby RD Carmel Perth WA.</span>
    </li>
    <li class="contact-item">
      <svg class="contact-icon" viewBox="0 0 18 20" aria-hidden="true">
        <rect x="4" y="1.5" width="10" height="17" rx="1.5" fill="none" stroke="var(--text-light)" stroke-width="2"/>
        <circle cx="9" cy="15" r="1.2" fill="var(--text-light)"/>
      </svg>
      <span>0438120957</span>
    </li>
    <li class="contact-item">
      <svg class="contact-icon" viewBox="0 0 18 20" aria-hidden="true">
        <rect x="1" y="5" width="16" height="11" fill="var(--text-light)"/>
        <polyline points="1,5 9,11 17,5" fill="none" stroke="var(--navy)" stroke-width="1.5"/>
        <polyline points="1,16 7,10 M17,16 11,10" fill="none" stroke="var(--navy)" stroke-width="1.2"/>
      </svg>
      <span>derek@ironvalemx.com</span>
    </li>
  </ul>
</section>

</body>
</html>
```